Plorvantix Redesign Website

Looking for a web design who can think out of the box.
Redesign of www.plorvantix.com.au.
Design requirements:
- Use of many different Colors based on icon logo
- Use of nature and animal pictures that symbolize evolution, transition, metamorphosis, change, etc.
- Website background color for each page is based on Icon logo
- Website mood: Transition & Change, Water, Natural cycle, Waves, Natural evolution, Circle, Wheel,
- Landing page design with animated grafik based on logo icon
- Define colorful design flow that incorporates the website content (see attached file)
- Website development in Wix, access will be provided after final design

Target Market(s)

Non-for-profits in Health and Social sector, local small businesses

Industry/Entity Type

Community Development, Health, Aged-Care,

Coding

Coded - Design and coding required

Number of Pages Required

5+ page

Font styles to use
Sans Serif
Other font styles liked:
• MavenPro, Futura,

Colors
00AB8E
00BBA5
67D7C9
C6EFE9
E9F9F6
FFC000
F8CF3A
FAE287
FDF2CF
FEFAEE
F0912C
F2A743
F7CA91
FBE8D2
FDF5EE

Requirements
Must have
• Landing page with animated grafik, responsive design, out-of-box design, all pages and functions on current website, animated text and design ellements on all sides,
Nice to have
• use logo icon for landing page; it would be great if icon could be animated for the landing page, e.g. moving circles that coming out ot the head
Should not have
• look like a wix template, center aligments in block desciptions, corporate look

```html
<!DOCTYPE html>
<html lang="en">
<head>
<meta charset="utf-8">
<title>Plorvantix — Change Management</title>
<link rel="stylesheet" href="https://fonts.googleapis.com/css2?family=Montserrat:wght@400;500;600;700&family=Oswald:wght@600&display=swap">
<style>
:root{
  --teal:#00AB8E;
  --teal-2:#00BBA5;
  --teal-3:#67D7C9;
  --teal-4:#C6EFE9;
  --teal-5:#E9F9F6;
  --teal-deep:#00806b;
  --yellow:#FFC000;
  --yellow-2:#F8CF3A;
  --yellow-3:#FAE287;
  --yellow-4:#FDF2CF;
  --cream:#FEFAEE;
  --orange:#F0912C;
  --orange-2:#F2A743;
  --orange-3:#F7CA91;
  --orange-4:#FBE8D2;
  --text:#333;
  --line:#bfbfbf;
}
*{box-sizing:border-box;margin:0;padding:0}
html,body{width:1200px;height:3929px;overflow:hidden}
body{position:relative;font-family:"Montserrat",sans-serif;color:var(--text);background:#fff}
.abs{position:absolute}
/* header */
.site-header{left:0;top:0;width:1200px;height:80px;background:#fff}
.brand{left:64px;top:22px;display:flex;align-items:center;gap:10px;font-weight:700;font-size:17px;color:#222}
.brand-dot{width:34px;height:34px;border-radius:50%;background:var(--orange)}
.nav{left:667px;top:33px;display:flex;font-size:12px;font-weight:600;letter-spacing:.5px}
.nav span{display:block;margin-right:48px}
.login{left:1045px;top:19px;width:125px;height:43px;background:var(--yellow);color:#222;font-size:12px;font-weight:700;display:flex;align-items:center;justify-content:center;box-shadow:0 3px 6px rgba(0,0,0,.2)}
/* hero */
.hero{left:0;top:80px;width:1200px;height:600px;background:linear-gradient(90deg,#b8c2ce 0%,#d5dbe2 30%,#d9a7c4 38%,#c97fb0 48%,#2fb33a 57%,#34b840 62%,#e8731c 68%,#d7651a 80%,#8fb4dc 100%)}
.hero-quote{left:170px;top:322px;width:860px;text-align:center;font-family:"Oswald",sans-serif;font-weight:600;font-size:38px;line-height:50px;color:#fff;letter-spacing:1px;text-shadow:0 2px 4px rgba(0,0,0,.3)}
.qmark{font-family:Georgia,serif;font-size:100px;color:#1b2a44;line-height:1;font-weight:700}
.hero-author{left:940px;top:446px;font-size:22px;font-weight:600;color:#fff;letter-spacing:3px}
/* intro */
.intro{left:220px;top:750px;width:760px;text-align:center;font-size:23px;line-height:41px;color:#555}
/* split rows */
.panel{width:615px;height:488px}
.panel-copy{padding:100px 40px 0 162px;color:#fff}
.panel-copy h2{font-size:24px;line-height:38px;font-weight:600;margin-bottom:18px;white-space:nowrap}
.panel-copy p{font-size:13px;line-height:24.5px;margin-bottom:10px}
.teal-panel{left:0;top:938px;background:linear-gradient(180deg,var(--teal-2),var(--teal))}
.teal-panel h2{color:var(--yellow-3)}
.photo-sea{left:615px;top:938px;width:585px;background:linear-gradient(180deg,#7ea9d6 0%,#6c8b76 30%,#3b6fa1 50%,#2b5f7a 70%,#6f8a62 100%)}
.photo-cherries{left:0;top:1426px;background:radial-gradient(circle at 50% 50%,#e94a3a 0,#f1a04a 18%,#fafafa 40%,#f4f4f4 100%)}
.yellow-panel{left:615px;top:1426px;width:585px;background:var(--yellow-2)}
.yellow-copy{padding:98px 178px 0 53px}
.yellow-copy h2{font-size:25px;color:var(--teal-deep);font-weight:600;margin-bottom:18px}
.yellow-copy h3{font-size:16px;font-weight:500;line-height:30px;color:#222;margin-bottom:18px}
.yellow-copy p{font-size:13px;line-height:24.5px;color:#333;margin-bottom:12px}
/* carousel */
.card{top:1990px;width:397px;height:300px;background:#fff;box-shadow:0 0 10px rgba(0,0,0,.12);padding:20px 22px}
.card-photo{width:353px;height:202px}
.card p{font-size:15px;line-height:24px;color:#222;margin-top:16px}
.arrow{border-radius:50%;display:flex;align-items:center;justify-content:center;box-shadow:0 3px 6px rgba(0,0,0,.25)}
.arrow.prev{background:var(--orange)}
.arrow.next{background:var(--teal)}
/* orange */
.orange-panel{left:0;top:2368px;height:487px;background:linear-gradient(180deg,var(--orange-2),var(--orange))}
.orange-panel .panel-copy{padding-top:42px}
.orange-panel h2{color:var(--cream)}
.orange-panel p a{color:#5a2a00;text-decoration:underline}
.photo-cliff{left:615px;top:2368px;width:585px;height:487px;background:linear-gradient(160deg,#b9b2a4 0%,#8c7460 45%,#c9a98a 75%,#a98d76 100%)}
/* testimonials */
.testimonials{left:0;top:2855px;width:1200px;height:400px;background:linear-gradient(180deg,var(--teal-4) 0%,var(--teal-5) 60%,#fbfefd 100%)}
.section-title{width:1200px;text-align:center;font-size:25px;font-weight:600;color:var(--teal-deep)}
.t-card{left:404px;top:3020px;width:392px;height:205px;background:#fff;box-shadow:0 0 10px rgba(0,0,0,.08);padding:26px 24px}
.t-card .big-q{position:absolute;left:14px;top:4px;font-family:Georgia,serif;font-size:80px;color:#ddd;line-height:1}
.t-card p{position:relative;font-size:13px;line-height:24.5px;color:#444}
.t-name{margin-top:14px;font-size:12px;font-weight:600;color:var(--teal)}
.t-role{font-size:12px;color:#777}
/* contact */
.contact-text{left:220px;top:3342px;width:760px;text-align:center;font-size:13px;line-height:25px;color:#555}
.field{border:1px solid var(--line);background:#fff;font-size:11px;color:#555;padding:14px 16px}
.submit{left:538px;top:3645px;width:124px;height:44px;background:var(--yellow);font-size:12px;font-weight:700;display:flex;align-items:center;justify-content:center;box-shadow:0 3px 6px rgba(0,0,0,.2)}
/* footer */
.site-footer{left:0;top:3752px;width:1200px;height:136px;background:var(--teal);color:#fff}
.f-item{display:flex;gap:8px;font-size:12px;line-height:20px;font-weight:500}
.f-brand{left:550px;top:28px;width:100px;text-align:center;font-weight:700;font-size:15px}
.f-brand .dot{width:28px;height:28px;border-radius:50%;background:var(--orange);margin:0 auto 8px}
.f-social{left:592px;top:100px;width:16px;height:16px;border-radius:50%;background:#fff}
.copyright{left:0;top:3888px;width:1200px;height:41px;text-align:center;font-size:12px;line-height:41px;color:#333}
</style>
</head>
<body>

<header class="abs site-header">
  <div class="abs brand"><span class="brand-dot"></span>Plorvantix</div>
  <nav class="abs nav"><span>HOME</span><span>ABOUT</span><span>SERVICE</span><span>CONTACT</span></nav>
  <div class="abs login">LOGIN</div>
</header>

<section class="abs hero" role="img" aria-label="A single tree shown across four seasons, from winter snow through spring blossom and summer green to autumn orange"></section>
<div class="abs" style="left:110px;top:310px"><span class="qmark">&#8220;</span></div>
<p class="abs hero-quote">Yesterday I was clever, so I wanted to change the world. Today I am wise, so I am changing myself.</p>
<div class="abs" style="left:1028px;top:376px"><span class="qmark">&#8221;</span></div>
<p class="abs hero-author">—Aurel</p>

<p class="abs intro">Our extensive care manager, community development and social work experience is the sole reason behind our thorough understanding of organisation.</p>

<section class="abs panel teal-panel">
  <div class="panel-copy">
    <h2>Our Learnings Over the Years<br>Technology Alone Won't Help You</h2>
    <p>Fortunately or unfortunately, the shiny technology isn't a silver bullet you have been searching for. New technology can get you only so far. The challenge here is transforming the mindsets, behaviours with the new ways of working.</p>
    <p>Hence, the combination of these two will lead to true organisational transformation. Improved performance is a combination of being effective, efficient, and technology.</p>
  </div>
</section>
<div class="abs panel photo-sea" role="img" aria-label="Split view of a tropical lagoon with limestone islands above and coral reef below the waterline"></div>

<div class="abs panel photo-cherries" role="img" aria-label="Cherries arranged in a circle on white, ripening from green to red"></div>
<section class="abs panel yellow-panel">
  <div class="yellow-copy">
    <h2>Non-bios System Review</h2>
    <h3>Are You Looking into a Client Management System and Don't Know Where to Begin?</h3>
    <p>Our team does requirement workshops with your key staff members. Based on the requirements, we do a tool based agnostic research which is the best-fit solution for you, minus provider bios.</p>
    <p>We also provide a tool-based evaluation of best-fit systems; CRM or LMS or other systems. Non-bios.</p>
  </div>
</section>

<div class="abs arrow prev" style="left:81px;top:2110px;width:56px;height:56px">
  <svg width="16" height="16" viewBox="0 0 16 16"><path d="M10 2 L4 8 L10 14" fill="none" stroke="#fff" stroke-width="2"/></svg>
</div>
<article class="abs card" style="left:188px">
  <div class="card-photo" role="img" aria-label="Seedlings sprouting from dark soil" style="background:linear-gradient(180deg,#a8b67a 0%,#6f8c3c 55%,#3b2a1c 80%,#2a1d14 100%)"></div>
  <p>Find the best-fit Client Management System for your organisation without bios</p>
</article>
<article class="abs card" style="left:615px">
  <div class="card-photo" role="img" aria-label="Turquoise wave breaking under a pink sunset sky" style="background:linear-gradient(180deg,#6a8fb0 0%,#e88a7a 40%,#f2a08a 55%,#2aa3c4 75%,#0f6d8f 100%)"></div>
  <p>Identify change impact and resistance</p>
</article>
<div class="abs arrow next" style="left:1059px;top:2110px;width:56px;height:56px">
  <svg width="16" height="16" viewBox="0 0 16 16"><path d="M6 2 L12 8 L6 14" fill="none" stroke="#fff" stroke-width="2"/></svg>
</div>

<section class="abs panel orange-panel">
  <div class="panel-copy">
    <h2>We are Committed to Our Local<br>Community Support!</h2>
    <p>We are purpose and people-driven. Think of us as a safe pair of hands. We have a community fund that supports local NFP. I also volunteer as a business coach for women with Kindred Circle organisation: <a>https://kindredcircle.org/</a></p>
    <p>We have extensive experience in working with government agencies and funding bodies. We have worked for aboriginal communities and organisations in northern territory.</p>
    <p>We are located in Byron Bay and provide also on-premises services to local NFPs in this region. We pride ourselves on our well-connected network of digital transformation and data experts in Australia and around the world, so our clients get the best-suited services and systems.</p>
  </div>
</section>
<div class="abs photo-cliff" role="img" aria-label="Traveller with a backpack seated on a rocky cliff looking out over the sea"></div>

<section class="abs testimonials" role="img" aria-label="Soft misty snow-covered mountain range"></section>
<h2 class="abs section-title" style="left:0;top:2928px">What do Our Clients Have to Say?</h2>
<div class="abs arrow prev" style="left:290px;top:3103px;width:40px;height:40px">
  <svg width="12" height="12" viewBox="0 0 16 16"><path d="M10 2 L4 8 L10 14" fill="none" stroke="#fff" stroke-width="2"/></svg>
</div>
<article class="abs t-card">
  <span class="big-q">&#8220;</span>
  <p>Truly the ultimate change management professionals. Their team even challenge your own way of thinking about certain aspects of the business and help you redefine ideas.</p>
  <div class="t-name">L. Ostrova</div>
  <div class="t-role">Care Manager Community Services</div>
</article>
<div class="abs arrow next" style="left:870px;top:3103px;width:40px;height:40px">
  <svg width="12" height="12" viewBox="0 0 16 16"><path d="M6 2 L12 8 L6 14" fill="none" stroke="#fff" stroke-width="2"/></svg>
</div>

<h2 class="abs section-title" style="left:0;top:3295px">Get in Touch with Us</h2>
<p class="abs contact-text">Faced with a project that requires change management? Simply fill out the form and our team will get back to you shortly. Not a fan of forms? A call (add number) or an email (add email) will work too.</p>
<div class="abs field" style="left:357px;top:3428px;width:234px;height:42px">First Name*</div>
<div class="abs field" style="left:612px;top:3428px;width:234px;height:42px">Last Name*</div>
<div class="abs field" style="left:357px;top:3481px;width:234px;height:42px">Email*</div>
<div class="abs field" style="left:612px;top:3481px;width:234px;height:42px">Phone *</div>
<div class="abs field" style="left:357px;top:3534px;width:489px;height:80px">Message*</div>
<div class="abs submit">Submit</div>

<footer class="abs site-footer">
  <div class="abs f-item" style="left:162px;top:42px">
    <svg width="14" height="14" viewBox="0 0 24 24"><path d="M6.6 10.8a15 15 0 0 0 6.6 6.6l2.2-2.2a1 1 0 0 1 1-.25 11.4 11.4 0 0 0 3.6.6 1 1 0 0 1 1 1V20a1 1 0 0 1-1 1A17 17 0 0 1 3 4a1 1 0 0 1 1-1h3.5a1 1 0 0 1 1 1 11.4 11.4 0 0 0 .6 3.6 1 1 0 0 1-.25 1z" fill="#FFC000"/></svg>
    <div>Phone:<br>+61400527194</div>
  </div>
  <div class="abs f-brand"><div class="dot"></div>Plorvantix</div>
  <div class="abs f-social"></div>
  <div class="abs f-item" style="left:816px;top:42px">
    <svg width="16" height="14" viewBox="0 0 24 20"><rect x="1" y="2" width="22" height="16" rx="2" fill="#FFC000"/><path d="M1 3 L12 11 L23 3" fill="none" stroke="#00AB8E" stroke-width="2"/></svg>
    <div>Email:<br>getintouch@plorvantix.com</div>
  </div>
</footer>
<p class="abs copyright">@2022 | Photography by Tessa Brune | All rights reserved</p>

</body>
</html>
```